Motive für Servietten - Länderservietten - Deutschland, Italien, Frankreich, Spanien und Griechenland
Zielgruppe
Wir sind Versandhändler aus dem Bereich Büro Basteln Schule und Geschenkartikel und verkaufen neben Handelsware aus diesem Bereich auch viele eigene selbst gestaltete Artikel unter unserem Firmennamen morvalo.
Aufgabenstellung
Gestaltet werden soll eine neue Motivserie für unsere Servietten
Thema sind hier Länderservietten
Passend für Feierlichkeiten die unter dem jeweiligen Land als Motto stehen oder auch für Veranstaltungen wie z.B. Fussball EM / WM
Basis sollte die Länderflaggen sein
Folgende Länder sollten im einheitlichen Designstil umgesetzt werden
Deutschland
Italien
Spanien
Frankreich
Griechenland
Rahmendaten zur Serviette
Größe: 30x30
Packung mit 20 Stück
Beispielfoto anbei
Ablauf im Wettbewerb
In der Wettbewerbsphase: Design des Motivs für die 5 Länder
Nach Abschluss des Wettbewerbs und Zuteilung des Gewinners:
-Erstellung der finalen Druckdateien (Beispiel Druckdatei anbei)
- Produktfotos alle Ansichten (Mockups können zur Verfügung gestellt werden)

```html
<!DOCTYPE html>
<html lang="it">
<head>
<meta charset="utf-8">
<title>Benvenuto – Serviettenmotiv Italien</title>
<link rel="stylesheet" href="https://fonts.googleapis.com/css2?family=Open+Sans:wght@400&display=swap">
<style>
  :root {
    --board-dark: #2c2c2c;
    --board-chalk: #4a4a4a;
    --board-mid: #3a3a3a;
    --flag-green: #2f8f48;
    --flag-white: #f6f7f9;
    --flag-red: #dc1f38;
    --greeting-red: #e8141c;
    --greeting-light: #f6f7f9;
  }
  html, body {
    margin: 0;
    padding: 0;
    width: 1200px;
    height: 1200px;
    overflow: hidden;
    background: var(--board-dark);
  }
  .napkin {
    position: relative;
    width: 1200px;
    height: 1200px;
    overflow: hidden;
  }
  .food-doodle-pattern {
    position: absolute;
    inset: 0;
    background:
      radial-gradient(ellipse at 30% 20%, var(--board-chalk), transparent 60%),
      radial-gradient(ellipse at 75% 85%, var(--board-chalk), transparent 60%),
      var(--board-mid);
  }
  .flag-stroke {
    position: absolute;
    left: 0;
    top: 0;
    width: 1200px;
    height: 1200px;
  }
  .flag-green { fill: var(--flag-green); }
  .flag-white { fill: var(--flag-white); }
  .flag-red { fill: var(--flag-red); }
  .greeting {
    position: absolute;
    left: 240px;
    top: 512px;
    margin: 0;
    white-space: nowrap;
    font-family: "Open Sans", sans-serif;
    font-weight: 400;
    font-size: 140px;
    line-height: 1;
    letter-spacing: 0;
    color: var(--greeting-red);
  }
  .greeting-on-red {
    color: var(--greeting-light);
  }
</style>
</head>
<body>
  <main class="napkin">
    <div class="food-doodle-pattern" role="img" aria-label="Weiße Kreidezeichnungen italienischer Speisen auf dunkler Tafel: Pizza, Weinflaschen, Pasta, Käse, Tomaten, Trauben, Oliven und Meeresfrüchte"></div>

    <svg class="flag-stroke" viewBox="0 0 1200 1200" aria-hidden="true">
      <polygon class="flag-green" points="
        420,372 300,380 230,398 210,430 160,445 170,500 120,520 140,560 98,600
        130,640 90,680 140,700 160,740 200,770 260,790 330,800 420,806"/>
      <polygon class="flag-white" points="420,372 804,380 804,792 420,806"/>
      <polygon class="flag-red" points="
        804,380 900,385 960,400 1000,430 985,470 1005,520 990,560 1008,610
        980,650 995,700 960,730 990,760 940,772 900,786 804,792"/>
    </svg>

    <h1 class="greeting">Benvenu<span class="greeting-on-red">to</span></h1>
  </main>
</body>
</html>
```